Brightfold Partners Website

Brightfold Partners Advisory Services is a company which provides specialised advise in carbon markets, climate policy, landscapes, resilience and change. We are based in Australia but the majority of our business is global. Our clients range from governments to large corporates and not for profit organisations.
Our focus is on developing the capabilities of government officials, business decision makers and land managers so they can better navigate the complexity of climate change and sustainability.
We are looking for a website that is consistent with the high end professional services which we provide to serious players.
I have attached two versions of our logo. I have also attached the back of our business card so you can get a sense of what we hand to potential clients.

Target Market(s)

Professional individuals, decision makers, board members etc, government officials.

Industry/Entity Type

Government

Number of Pages Required

4 page

Font styles to use
Serif
Sans Serif

Requirements
Must have
• Please provide
• 1. Home page
• 2. Service page template
• 3. Contact page
• 4. Lead expert profile page

```html
<!DOCTYPE html>
<html lang="en">
<head>
<meta charset="utf-8">
<title>Tom Haskell - Lead Expert | Brightfold Partners</title>
<link rel="stylesheet" href="https://fonts.googleapis.com/css2?family=Gelasio&family=Lato:wght@300;400&display=swap">
<style>
  :root {
    --page-bg: #ffffff;
    --panel-bg: #f8f8f8;
    --brand-teal: #1d4f59;
    --button-teal: #1e5761;
    --body-text: #3a3a3a;
    --rule: #dedede;
    --portrait-light: #d9d9d9;
    --portrait-dark: #8a8a8a;
  }
  * { box-sizing: border-box; margin: 0; padding: 0; }
  html, body {
    width: 1200px; height: 900px; overflow: hidden;
    background: var(--page-bg);
  }
  .profile-section {
    position: absolute; left: 0; top: 32px;
    width: 1200px; height: 828px;
    background: var(--panel-bg);
  }
  .profile-title {
    position: absolute; left: 0; top: 58px; width: 1200px;
    text-align: center;
    font-family: "Gelasio", Georgia, serif;
    font-weight: 400; font-size: 22px;
    color: var(--brand-teal);
  }
  .title-rule, .footer-rule {
    position: absolute; left: 462px; width: 276px; height: 1px;
    background: var(--rule);
  }
  .title-rule { top: 109px; }
  .footer-rule { top: 711px; }
  .profile-body {
    position: absolute; left: 245px; top: 143px; width: 722px;
    font-family: "Lato", Arial, sans-serif;
    font-weight: 300; font-size: 18px; line-height: 35.5px;
    color: var(--body-text);
  }
  .profile-body p + p { margin-top: 35.5px; }
  .portrait {
    float: left;
    width: 273px; height: 272px;
    margin: 18px 32px 4px 0;
    border-radius: 50%;
    background: radial-gradient(circle at 55% 40%, var(--portrait-light), var(--portrait-dark));
  }
  .services-link {
    color: var(--brand-teal); font-weight: 400; text-decoration: none;
  }
  .read-more {
    position: absolute; left: 513px; top: 711px;
    width: 176px; height: 28px;
    background: var(--button-teal);
    color: #ffffff;
    font-family: "Lato", Arial, sans-serif;
    font-weight: 300; font-size: 18px; line-height: 28px;
    text-align: center; text-decoration: none;
    box-shadow: 0 2px 5px rgba(0,0,0,0.25);
  }
</style>
</head>
<body>
  <section class="profile-section">
    <h1 class="profile-title">Tom Haskell - Lead Expert</h1>
    <div class="title-rule"></div>
    <div class="profile-body">
      <div class="portrait" role="img" aria-label="Portrait photograph of the lead expert"></div>
      <p>Tom Haskell is recognized globally as an expert in climate policy, carbon markets and their impact on business.&nbsp; Over the last decade he has provided advice to a wide range of organisations, including the UN, governments, regulators, major corporations, international banks, service providers, industry associations and non-profit organisations. His experience and expertise is focused on the detailed design and implementation of carbon market mechanisms, development of robust reporting and verification regimes, and preparing government and business decision makers for their role in a carbon constrained global economy.</p>
      <p>Tom has undertaken a wide variety of engagements since his carbon career began in 2002.&nbsp; The activities summarized on the <a class="services-link" href="#">Services</a> pages demonstrate his breadth of…</p>
    </div>
    <div class="footer-rule"></div>
    <a class="read-more" href="#">Read more</a>
  </section>
</body>
</html>
```